LumeWear e-commerce website design for cartwell platform

I currently have a trendy e-commerce clothing store that is primarily based off of the Southern California Style/Trends. I am looking for a redesign of my cartwell template as I don't like my current image. I am looking for a sleek clean design that allows more focus on the products. I like neutral backgrounds and easy to use websites. Should be responsive to mobile devices. I would also like to have some ideas for a slide show picture that notifies customers of free shipping if possible. I do also have a theme template that I purchased through Cartwell so one could set the theme up for me and edit it to what I need. My website is lumewear.example if you would like to look at the type of products I have. I am also looking to do a logo redesign as well- looking for a more stylish logo that would appeal to an approximate age range of 18-40 year old women. I want to be remembered, something to match the web design.

I like teal/turquoise and grey combos but I don't have to have this as the colors.

Target Market(s)

approx. 18-40

Industry/Entity Type

E-Commerce

Number of Pages Required

2 page

Requirements
Must have
• Menu bar, cartwell compatible, easy to access/navigate, responsive to mobile devices, easy product upload
Nice to have
• if able ability to resize pictures all to the same size
Should not have
• not be difficult to navigate both on a reg. computer or mobile device

```html
<!DOCTYPE html>
<html lang="en">
<head>
<meta charset="utf-8">
<title>LumeWear – Storefront</title>
<link rel="stylesheet" href="https://fonts.googleapis.com/css2?family=Roboto:wght@300;400;500;700&family=Playfair+Display:wght@700&display=swap">
<style>
  :root{
    --teal:#2f9ea8;
    --teal-dark:#2c6a74;
    --teal-btn:#1fa3b0;
    --yellow:#e9b928;
    --navy:#36486a;
    --page:#ececec;
    --card:#ffffff;
    --ink:#333333;
    --muted:#9a9a9a;
    --accent:#e0533f;
    --purple:#9c3d9f;
    --green:#62cf5b;
    --stone:#5f5658;
  }
  *{box-sizing:border-box;margin:0;padding:0}
  html,body{width:1200px;height:1200px;overflow:hidden}
  body{background:var(--page);font-family:"Roboto",Arial,sans-serif;color:var(--ink)}

  .top-bar{height:92px;background:var(--teal);display:flex;align-items:center;padding:0 60px;gap:34px}
  .brand{display:flex;align-items:center;gap:10px;color:#fff;font-size:30px;font-weight:500;letter-spacing:.5px;white-space:nowrap}
  .brand-dot{width:14px;height:14px;border-radius:50%;background:#fff}
  .search{display:flex;height:40px;width:560px}
  .search-field{flex:1;background:#fff;border:none;padding:0 16px;font:400 14px "Roboto",sans-serif;color:#aaa;display:flex;align-items:center}
  .search-btn{width:120px;background:var(--yellow);color:#fff;font-weight:700;font-size:14px;display:flex;align-items:center;justify-content:center;letter-spacing:.5px}
  .account{margin-left:auto;color:#fff;font-size:14px;white-space:nowrap}

  .main-nav{height:50px;background:var(--teal-dark);display:flex;align-items:center;padding:0 60px;gap:38px;color:#fff;font-size:14px;font-weight:500;letter-spacing:.3px}
  .main-nav .cat{display:flex;align-items:center;gap:7px}

  .hero{display:flex;gap:26px;padding:30px 60px 0}
  .slider{position:relative;width:764px;height:392px;overflow:hidden}
  .slide-photo{position:absolute;inset:0;background:linear-gradient(100deg,#8a6a44 0%,#b49570 30%,#d9d2c8 48%,#4a3a32 62%,#e8e4e0 78%,#9a8870 100%)}
  .sale-box{position:absolute;left:56px;top:42px;width:256px;height:292px;background:var(--yellow);color:#fff;text-align:center}
  .sale-title{font-family:"Playfair Display",Georgia,serif;font-size:46px;padding-top:14px;height:88px;letter-spacing:1px}
  .sale-band{background:var(--navy);height:60px;display:flex;align-items:center;justify-content:center;font-size:27px;font-weight:300}
  .sale-note{font-size:13px;line-height:18px;padding:22px 18px 0;text-transform:uppercase}
  .sale-cta{display:inline-block;margin-top:18px;background:var(--teal-btn);padding:8px 16px;font-size:12px;font-weight:700}
  .arrow{position:absolute;top:162px;width:34px;height:52px;background:rgba(20,20,20,.8);display:flex;align-items:center;justify-content:center}
  .arrow.prev{left:0}.arrow.next{right:0}

  .sidebar{width:290px;display:flex;flex-direction:column}
  .offer{background:var(--purple);color:#fff;padding:12px 16px}
  .offer h3{font-size:19px;font-weight:400;white-space:nowrap}
  .offer h3 b{font-weight:700}
  .offer p{font-size:11px;margin-top:4px}
  .newsletter{background:#fff;padding:14px 16px 16px}
  .newsletter h4{font-size:14px;font-weight:400}
  .email{margin-top:10px;border:1px solid #ddd;height:28px;font-size:11px;color:#bbb;padding:6px 10px}
  .signup{margin-top:12px;display:inline-block;background:var(--teal-btn);color:#fff;font-size:12px;font-weight:700;padding:6px 12px}
  .badge{flex:1;min-height:70px}
  .badge.primary{background:var(--green)}
  .badge.secondary{background:var(--stone)}

  .section-title{margin:34px 60px 0;color:var(--accent);font-size:32px;font-weight:400;padding-bottom:10px;border-bottom:3px solid var(--accent)}
  .categories{display:grid;grid-template-columns:repeat(3,1fr);gap:18px 22px;padding:24px 60px 0}
  .category{background:var(--card);height:86px;display:flex;align-items:center;gap:18px;padding:0 22px}
  .category svg{flex:none;width:34px;height:34px}
  .category h5{font-size:21px;font-weight:400;color:#222;white-space:nowrap}
  .category p{font-size:13px;color:var(--muted);margin-top:4px;white-space:nowrap}
</style>
</head>
<body>
  <header class="top-bar">
    <div class="brand"><span class="brand-dot"></span>LumeWear</div>
    <div class="search">
      <div class="search-field">Search for a product, category or brand</div>
      <div class="search-btn">SEARCH</div>
    </div>
    <div class="account">Log in | Sign up | Dutch ▾</div>
  </header>

  <nav class="main-nav">
    <span class="cat">
      <svg width="12" height="12" viewBox="0 0 12 12" fill="#fff"><rect width="3" height="3"/><rect x="4.5" width="3" height="3"/><rect x="9" width="3" height="3"/><rect y="4.5" width="3" height="3"/><rect x="4.5" y="4.5" width="3" height="3"/><rect x="9" y="4.5" width="3" height="3"/><rect y="9" width="3" height="3"/><rect x="4.5" y="9" width="3" height="3"/><rect x="9" y="9" width="3" height="3"/></svg>
      CATEGORIES ▾</span>
    <span>WHAT'S NEW</span><span>SALE</span><span>ABOUT US</span><span>CONTACT US</span>
  </nav>

  <section class="hero">
    <div class="slider">
      <div class="slide-photo" role="img" aria-label="Fashion photo of a couple in winter clothing inside a boutique"></div>
      <div class="sale-box">
        <div class="sale-title">SALE</div>
        <div class="sale-band">Up to 50% off</div>
        <div class="sale-note">This offer is valid on<br>all XYZ brands.</div>
        <span class="sale-cta">ADD TO CART ›</span>
      </div>
      <div class="arrow prev"><svg width="12" height="18" viewBox="0 0 12 18"><path d="M9 2 2 9l7 7" stroke="#fff" stroke-width="2.4" fill="none"/></svg></div>
      <div class="arrow next"><svg width="12" height="18" viewBox="0 0 12 18"><path d="M3 2l7 7-7 7" stroke="#fff" stroke-width="2.4" fill="none"/></svg></div>
    </div>

    <aside class="sidebar">
      <div class="offer">
        <h3><b>Free</b> Discount on LumeWear</h3>
        <p>• Find items &nbsp;• use it &nbsp;• Enjoy it</p>
      </div>
      <div class="newsletter">
        <h4>Get LumeWear by Email</h4>
        <div class="email">Enter your email here</div>
        <span class="signup">SIGN UP NOW ›</span>
      </div>
      <div class="badge primary" role="img" aria-label="Mobile app download badge"></div>
      <div class="badge secondary" role="img" aria-label="Second mobile app download badge"></div>
    </aside>
  </section>

  <h2 class="section-title">Popular Categories</h2>
  <section class="categories">
    <div class="category">
      <svg viewBox="0 0 34 34"><rect x="3" y="14" width="6" height="16" fill="#f26b1d"/><path d="M11 14l6-10c3 0 4 2 3 5l-1 4h9c2 0 3 2 2 4l-3 11c-1 2-2 2-4 2H11z" fill="#f26b1d"/></svg>
      <div><h5>Deals &amp; Offers</h5><p>Top Deals &amp; offers across 100+ Stores</p></div>
    </div>
    <div class="category">
      <svg viewBox="0 0 34 34"><path d="M12 4h10l4 5c-2 2-6 2-9 2s-7 0-9-2z" fill="#2fb3c0"/><path d="M11 11h12l-2 7 6 12H7l6-12z" fill="#2fb3c0"/></svg>
      <div><h5>Fashion Clothing</h5><p>Top Deals &amp; offers across 100+ Stores</p></div>
    </div>
    <div class="category">
      <svg viewBox="0 0 34 34"><path d="M4 10l6 6 7-9 7 9 6-6-3 16H7z" fill="#2bb6a3"/><rect x="7" y="27" width="20" height="3" fill="#2bb6a3"/></svg>
      <div><h5>Fashion Accessories</h5><p>Top Deals &amp; offers across 100+ Stores</p></div>
    </div>
    <div class="category">
      <svg viewBox="0 0 34 34"><path d="M12 5l-9 5 3 6 4-2v15h14V14l4 2 3-6-9-5c-1 3-3 4-5 4s-4-1-5-4z" fill="#ee6e8a"/></svg>
      <div><h5>Tops</h5><p>Top Deals &amp; offers across 100+ Stores</p></div>
    </div>
    <div class="category">
      <svg viewBox="0 0 34 34"><path d="M4 28c0-3 2-4 6-5l6-13c1-2 3-2 4 0l2 5c1 4 6 6 9 8v5H19l-3-6-5 6z" fill="#1f4fb3"/></svg>
      <div><h5>Shoes Accessories</h5><p>Top Deals &amp; offers across 100+ Stores</p></div>
    </div>
    <div class="category">
      <svg viewBox="0 0 34 34"><path d="M13 3h8v5l-1 4 7 18H7l7-18-1-4z" fill="#e04f8a"/></svg>
      <div><h5>Dresses</h5><p>Top Deals &amp; offers across 100+ Stores</p></div>
    </div>
    <div class="category">
      <svg viewBox="0 0 34 34"><path d="M9 3h16v7l-2 20h-4l-2-16-2 16h-4L9 10z" fill="#1e77d2"/></svg>
      <div><h5>Bottoms / Rompers</h5><p>Top Deals &amp; offers across 100+ Stores</p></div>
    </div>
    <div class="category">
      <svg viewBox="0 0 34 34"><path d="M13 5h8l8 6-2 18h-6V15l-4 3-4-3v14H7L5 11z" fill="#4aae6f"/></svg>
      <div><h5>Ethnic Wear</h5><p>Top Deals &amp; offers across 100+ Stores</p></div>
    </div>
    <div class="category">
      <svg viewBox="0 0 34 34"><rect x="14" y="3" width="6" height="11" fill="#6b4a2e"/><rect x="11" y="14" width="12" height="17" rx="2" fill="#b4552c"/></svg>
      <div><h5>Personal Care</h5><p>Top Deals &amp; offers across 100+ Stores</p></div>
    </div>
  </section>

  <h2 class="section-title">What's New!</h2>
</body>
</html>
```